Crestline Delivery Partners Business Card Redesign Project

CRESTLINE DELIVERY PARTNERS
Our company needs to have its business cards redesigned as the current design no longer reflects the business brand or attracts the type of clientele we are seeking.

MUST LOOK
★ Upmarket
★ Reflect Quality
★ Corporate feel
★ Professional
★ Innovative
★ Colourful

MUST PROMOTE
★ Market Leader
★ Knowledge
★ Expertise
★ Experience
★ Solutions
★ Advice

MUST FEEL
★ Classy
★ Elegant
★ Savvy
★ Edgy
★ Upbeat

WHAT WE DO
Crestline Delivery Partners provides project management and project controls consultancy services to companies in many industry sectors, within Australia and overseas. My company has developed a business brand through forging strong business relationships within industry. We provide innovative tools, concepts and solutions to management teams to assist them in better plan and managing there project portfolios.

SECTORS OF INDUSTRY WE SERVICE
★Oil & Gas
★Minerals & Metals
★Petrochemical
★Manufacturing
★Building & Construction
★Telecommunications
★Rail
★Civil

BUSINESS CARD DETAILS REQUIRED ON FRONT
Marcus Feldwick
Business Owner
Tel: 0498357162
Email: marcusfeldwick@crestlinedeliverypartners.com
Website: www.crestlinedeliverypartners.com.au

BUSINESS CARD DETAILS REQUIRED ON BACK
Providing | Knowledge | Expertise | Experience

ATTACHMENTS
Business Logo

Target Market(s)

Oil & Gas I Mining & Resources I Industry in General
Upmarket Clientele
Corporate World

Industry/Entity Type

Industry

Requirements
Must have
• Must be creative and a unique design
The business card must have information on the front and back

```html
<!DOCTYPE html>
<html lang="en">
<head>
<meta charset="utf-8">
<title>Crestline Delivery Partners – Business Card</title>
<link rel="stylesheet" href="https://fonts.googleapis.com/css2?family=Carlito:wght@400;700&family=Arimo:wght@400;700&display=swap">
<style>
  :root {
    --backdrop: #5b5b5b;
    --card-top: #ffffff;
    --card-bottom: #d6d6d6;
    --ink: #111111;
    --brand-red: #e0121c;
    --band-dark-top: #3a3a3a;
    --band-dark-bottom: #141414;
    --band-red-light: #d0161d;
    --band-red-deep: #8e0c12;
    --text-light: #e8e8e8;
    --white: #ffffff;
  }
  * { margin: 0; padding: 0; box-sizing: border-box; }
  html, body {
    width: 1200px;
    height: 776px;
    overflow: hidden;
    background: var(--backdrop);
  }
  .card {
    position: absolute;
    left: 231px;
    top: 174px;
    width: 738px;
    height: 428px;
    background: linear-gradient(180deg, var(--card-top) 0%, var(--card-bottom) 100%);
    box-shadow: 0 6px 18px rgba(0,0,0,0.35);
    overflow: hidden;
    font-family: "Carlito", "Calibri", sans-serif;
  }
  .brand {
    position: absolute;
    left: 34px;
    top: 118px;
    display: flex;
    align-items: center;
    gap: 16px;
  }
  .brand-mark {
    width: 40px;
    height: 40px;
    background: var(--brand-red);
    flex: none;
  }
  .brand-name {
    font-family: "Carlito", "Calibri", sans-serif;
    font-weight: 700;
    font-size: 44px;
    line-height: 1;
    color: var(--ink);
    letter-spacing: 0.5px;
    white-space: nowrap;
  }
  .tagline {
    position: absolute;
    left: 90px;
    top: 180px;
    font-family: "Arimo", "Arial", sans-serif;
    font-size: 16px;
    color: var(--ink);
    white-space: nowrap;
  }
  .band {
    position: absolute;
    left: 0;
    top: 300px;
    width: 738px;
    height: 128px;
  }
  .contact {
    position: absolute;
    left: 13px;
    top: 318px;
    list-style: none;
    color: var(--text-light);
    font-size: 16.5px;
    line-height: 28.5px;
    white-space: nowrap;
  }
  .person {
    position: absolute;
    right: 13px;
    top: 343px;
    text-align: right;
    color: var(--white);
  }
  .person-name {
    font-weight: 700;
    font-size: 29px;
    line-height: 1.2;
  }
  .person-role {
    font-size: 19px;
    line-height: 1.4;
  }
</style>
</head>
<body>
  <article class="card">
    <div class="brand">
      <span class="brand-mark"></span>
      <span class="brand-name">CRESTLINE DELIVERY PARTNERS</span>
    </div>
    <p class="tagline">Providing Effective Project Controls and Management Solutions</p>

    <svg class="band" viewBox="0 0 738 128" aria-hidden="true">
      <defs>
        <linearGradient id="bandRed" x1="0" y1="0" x2="1" y2="0">
          <stop offset="0" stop-color="var(--band-red-deep)"/>
          <stop offset="0.45" stop-color="var(--band-red-light)"/>
          <stop offset="1" stop-color="var(--band-red-light)"/>
        </linearGradient>
        <linearGradient id="bandDark" x1="0" y1="0" x2="0" y2="1">
          <stop offset="0" stop-color="var(--band-dark-top)"/>
          <stop offset="1" stop-color="var(--band-dark-bottom)"/>
        </linearGradient>
      </defs>
      <rect x="393" y="30" width="345" height="98" fill="url(#bandRed)"/>
      <polygon points="0,0 367,0 472,128 0,128" fill="url(#bandDark)"/>
    </svg>

    <ul class="contact">
      <li>Tel: 0498357162</li>
      <li>Email: marcusfeldwick@crestlinedeliverypartners.com</li>
      <li>Website: www.crestlinedeliverypartners.com.au</li>
    </ul>

    <div class="person">
      <p class="person-name">Marcus Feldwick</p>
      <p class="person-role">Business Owner</p>
    </div>
  </article>
</body>
</html>
```